Business card design for a engineering company

I need a double sided business card design for my company "Verdmont Flow Solutions". The card will be used in Malaysia. Sleek and professional, with a little design flare to it.
Information to showcase:
1. Company logo
2. Name, title, phone, email address, website address
3. our products "Pumping technology, Valve & actuation, Air Moving Technology
Example:
Ravi Tanaka
Business manager
ravi.tanaka@verdmont-example.com
www.verdmont-example.com.my
- Pumping technology
- Valve & actuation
- Air moving technology
Target Market(s)
engineers, purchasing managers
Industry/Entity Type
Business
Contact Information for Business Card
Ravi Tanaka
Business manager
ravi.tanaka@verdmont-example.com
www.verdmont-example.com.my
- Pumping technology
- Valve & actuation
- Air moving technology
catch phrase : "Solving flow challenges, exceeding expectations"

```html
<!DOCTYPE html>
<html lang="en">
<head>
<meta charset="utf-8">
<title>Verdmont Flow Solutions – Business Card</title>
<link rel="stylesheet" href="https://fonts.googleapis.com/css2?family=Questrial&family=Arimo:wght@400&display=swap">
<style>
  :root {
    --navy: #0e2b39;
    --orange: #e8832f;
    --card-white: #f4f4f4;
    --backdrop: #2e2e2e;
    --text-light: #ffffff;
    --text-dark: #1b1b1b;
  }
  html, body {
    margin: 0;
    padding: 0;
    width: 1200px;
    height: 965px;
    overflow: hidden;
    background: var(--backdrop);
  }
  .canvas {
    position: relative;
    width: 1200px;
    height: 965px;
  }
  .card {
    position: absolute;
    left: 246px;
    width: 710px;
    height: 404px;
    border-radius: 24px;
    overflow: hidden;
    background: radial-gradient(ellipse at 50% 40%, #ffffff 0%, var(--card-white) 60%, #e6e6e6 100%);
    box-shadow: 0 6px 18px rgba(0,0,0,0.45);
  }
  .card--front { top: 60px; }
  .card--back { top: 504px; }
  .card svg { position: absolute; inset: 0; display: block; }
  .brand-name { font-family: "Questrial", sans-serif; fill: var(--navy); }
  .info { font-family: "Arimo", sans-serif; fill: var(--text-light); }
  .products { font-family: "Arimo", sans-serif; fill: var(--text-dark); }
</style>
</head>
<body>
<main class="canvas">

  <section class="card card--front" aria-label="Business card front">
    <svg viewBox="0 0 710 404" width="710" height="404">
      <rect class="panel-dark" width="710" height="404" fill="var(--navy)"/>
      <path class="accent-line" d="M0 0 H355 Q446 200 350 404" fill="none" stroke="#ffffff" stroke-width="2"/>
      <path class="accent-band" d="M0 0 H350 Q440 200 345 404 H0 Z" fill="var(--orange)"/>
      <path class="accent-inner" d="M0 0 H306 Q445 205 335 404 H0 Z" fill="var(--navy)"/>
      <path class="panel-light" d="M0 0 H306 Q450 210 298 404 H0 Z" fill="var(--card-white)"/>

      <g class="brand">
        <circle cx="56" cy="202" r="22" fill="var(--navy)"/>
        <text class="brand-name" x="88" y="210" font-size="21">Verdmont Flow Solutions</text>
      </g>

      <g class="contact">
        <text class="info" x="427" y="92" font-size="22">Ravi Tanaka</text>
        <text class="info" x="427" y="114" font-size="16">Business manager</text>

        <path class="icon-phone" d="M432 177 q2 -2 4 0 l2 3 q1 2 -1 3 q1 3 4 5 q1 -2 3 -1 l3 2 q2 2 0 4 l-2 1 q-5 0 -10 -6 q-4 -5 -3 -9 z" fill="#ffffff"/>
        <text class="info" x="453" y="188" font-size="15.5">+60 3 5550 0147</text>

        <g class="icon-mail" fill="none" stroke-width="1.4">
          <rect x="430" y="199" width="15" height="10" fill="#ffffff" stroke="none"/>
          <path d="M430 199 L437.5 205 L445 199" stroke="var(--navy)"/>
          <path d="M430 209 L435.5 204 M445 209 L439.5 204" stroke="var(--navy)"/>
        </g>
        <text class="info" x="453" y="208" font-size="14">ravi.tanaka@verdmont-example.com</text>

        <g class="icon-globe" fill="none" stroke="#ffffff" stroke-width="1.1">
          <circle cx="437.5" cy="223" r="7"/>
          <ellipse cx="437.5" cy="223" rx="3" ry="7"/>
          <path d="M430.5 223 H444.5 M432 219 H443 M432 227 H443"/>
        </g>
        <text class="info" x="453" y="228" font-size="14">www.verdmont-example.com.my</text>

        <text class="info" x="431" y="298" font-size="15.5">Here your company or</text>
        <text class="info" x="431" y="318" font-size="15.5">home address</text>
      </g>
    </svg>
  </section>

  <section class="card card--back" aria-label="Business card back">
    <svg viewBox="0 0 710 404" width="710" height="404">
      <g class="brand">
        <circle cx="110" cy="156" r="36" fill="var(--navy)"/>
        <text class="brand-name" x="162" y="169" font-size="36">Verdmont Flow Solutions</text>
      </g>

      <text class="products" x="355" y="286" font-size="17" text-anchor="middle" xml:space="preserve">Pumping technology  |  Valve &amp; actuation  |  Air moving technology</text>

      <path class="swoosh-dark" d="M0 280 Q360 425 710 284 V404 H0 Z" fill="var(--navy)"/>
      <path class="swoosh-line" d="M0 316 Q380 418 710 288" fill="none" stroke="#ffffff" stroke-width="2"/>
      <path class="swoosh-band" d="M0 320 Q380 422 710 292 V328 Q380 417 0 326 Z" fill="var(--orange)"/>
    </svg>
  </section>

</main>
</body>
</html>
```